Post Card

We are looking for a design using our branding (harlowpipeworks.net). We would like 6x9 post card size. Scalable is preferred. Front side would be branding with 2-3 locations to add a special. Back would have services we offer listed with location for postage address.

Target Market(s)

New customers

Industry/Entity Type

Plumbing

Colors

Designer to choose colors to be used in the design.

```html
<!DOCTYPE html>
<html lang="en">
<head>
<meta charset="utf-8">
<title>Harlow Pipeworks Postcard</title>
<link href="https://fonts.googleapis.com/css2?family=Poppins:wght@400;500;600;700;800;900&family=Allura&display=swap" rel="stylesheet">
<style>
:root{
  --page:#a8a8a8;
  --navy:#0b2a66;
  --blue:#1646b4;
  --royal:#1f57d6;
  --yellow:#f0d31a;
  --red:#df2a2e;
  --pale:#c9dcfa;
  --white:#ffffff;
  --ink:#111827;
}
*{box-sizing:border-box;margin:0;padding:0}
html,body{width:888px;height:1200px;overflow:hidden}
body{background:var(--page);font-family:"Poppins",sans-serif;position:relative}
.card{position:absolute;left:89px;width:710px;height:473px;background:var(--white);overflow:hidden;box-shadow:0 6px 14px rgba(0,0,0,.3)}
.front{top:104px}
.back{top:623px}
.abs{position:absolute}

/* front */
.front-hero{left:0;top:0;width:710px;height:348px;background:linear-gradient(120deg,#0a2a6e 0%,#103a8f 55%,#1a4fa8 100%)}
.photo-plumber{left:300px;top:0;width:410px;height:257px;background:linear-gradient(135deg,#e8e6e2 0%,#f4f3f1 45%,#c9b59c 100%);clip-path:polygon(22% 60%,30% 0,100% 0,100% 100%,0 100%)}
.kicker{left:64px;top:36px;color:var(--white);font-weight:800;font-size:19px;letter-spacing:3px}
.headline{left:34px;top:56px;color:var(--yellow);font-weight:900;font-size:48px;line-height:46px;letter-spacing:-1px}
.script{left:106px;top:118px;color:var(--white);font-family:"Allura",cursive;font-size:42px}
.audience{left:36px;top:170px;color:var(--white);font-weight:800;font-size:25px;display:flex;align-items:center;gap:6px;letter-spacing:-.5px}
.or-dot{width:25px;height:25px;border-radius:50%;background:var(--yellow);color:var(--navy);font-size:10px;display:flex;align-items:center;justify-content:center}
.tagline{left:35px;top:213px;color:var(--white);font-weight:600;font-size:12.5px}
.tagline span{color:var(--yellow)}
.serving{left:38px;top:249px;width:169px;height:22px;border:1px solid #7ea3ee;background:var(--blue);color:var(--white);font-weight:700;font-size:12px;display:flex;align-items:center;justify-content:center}
.serving span{color:var(--yellow)}
.towns{left:38px;top:281px;display:grid;grid-template-columns:87px 100px;row-gap:3px;color:var(--white);font-size:11.5px}
.towns li{list-style:none;display:flex;align-items:center;gap:4px}
.perks{left:245px;top:257px;width:465px;height:110px;background:var(--yellow);border-radius:55px 0 0 55px;display:flex;padding-left:14px;padding-right:96px}
.perk{flex:1;display:flex;flex-direction:column;align-items:center;text-align:center;font-size:11.5px;line-height:13px;color:var(--ink);border-right:1px dashed #8a7a10;margin:10px 0;padding-top:4px}
.perk:last-child{border-right:none}
.perk-icon{width:28px;height:28px;border-radius:50%;background:var(--blue);border:2px solid var(--white);box-shadow:0 0 0 1px var(--blue);margin-bottom:7px}
.special{left:599px;top:244px;width:72px;height:183px;background:var(--red);clip-path:polygon(0 0,100% 0,100% 100%,50% 85%,0 100%);text-align:center;color:var(--white)}
.special-top{background:var(--blue);margin:6px 3px 0;padding:2px 0;font-weight:800;font-size:8px;line-height:9px;color:var(--white)}
.special-offer{margin-top:10px;font-weight:800;font-size:15px;line-height:15px;color:var(--yellow)}
.special-offer sup{font-size:8px}
.special-sub{font-size:9px;line-height:10px;font-weight:700;color:var(--yellow)}
.special-sub b{color:var(--white)}
.special-note{margin:8px 6px 0;border-top:1px dashed rgba(255,255,255,.6);padding-top:5px;font-size:6px;line-height:7.5px}
.brand{display:flex;align-items:center;gap:8px;font-weight:800;color:var(--navy);letter-spacing:.5px;white-space:nowrap}
.brand-dot{width:14px;height:14px;border-radius:50%;background:var(--blue)}
.front-brand{left:38px;top:392px;font-size:16px}
.cta{color:var(--blue);font-weight:800;font-size:17px;line-height:18px;white-space:nowrap}
.cta small{display:block;color:var(--ink);font-size:12.5px;font-weight:700}
.front-cta{left:255px;top:394px}
.contact{font-size:12px;font-weight:500;color:var(--ink);line-height:18px;white-space:nowrap}
.contact li{list-style:none;display:flex;align-items:center;gap:5px}
.front-contact{left:408px;top:397px}

/* back */
.back-hero{left:0;top:0;width:710px;height:347px;background:linear-gradient(110deg,#0a2a66 0%,#103c8c 60%,#1b55ad 100%)}
.services-tab{left:0;top:37px;width:301px;height:40px;background:var(--yellow);border-radius:0 22px 22px 0;color:var(--blue);font-weight:900;font-size:23px;display:flex;align-items:center;padding-left:38px;letter-spacing:.5px}
.services-title{left:313px;top:44px;color:var(--white);font-weight:800;font-size:19px}
.service{width:200px}
.service-head{position:relative;height:22px;background:var(--blue);border:1px solid #6f96ea;border-radius:0 12px 12px 0;margin-left:14px;color:var(--white);font-weight:700;font-size:12px;display:flex;align-items:center;padding-left:22px;white-space:nowrap}
.service-icon{position:absolute;left:-16px;top:-5px;width:30px;height:30px;border-radius:50%;background:var(--yellow);border:2px solid var(--navy)}
.service ul{margin-top:9px;width:222px;list-style:none;color:var(--white);font-size:10.5px;line-height:12.5px}
.service li{display:flex;gap:5px;margin-bottom:7px}
.tick{flex:none;margin-top:2px}
.col-rule{width:0;border-left:1px dashed rgba(255,255,255,.35)}
.row-rule{height:0;border-top:1px dashed rgba(255,255,255,.35)}
.trust{left:38px;top:347px;width:540px;height:37px;background:var(--pale);border-radius:0 0 0 18px;display:flex;align-items:center;font-weight:600;font-size:11px;color:var(--navy);white-space:nowrap}
.trust div{display:flex;align-items:center;gap:5px;padding:0 14px;height:100%;border-left:1px solid #a8c3f0}
.trust .trust-name{color:var(--blue);font-weight:800;font-size:10.5px;border-left:none;padding-left:14px;width:182px;background:#dae6fb;border-radius:0 0 0 18px}
.van{left:560px;top:334px;width:150px;height:76px;background:linear-gradient(160deg,#f3f5f9 0%,#d7dee9 60%,#2f63c8 100%);clip-path:polygon(14% 10%,100% 0,100% 85%,8% 100%,0 55%)}
.hours{left:38px;top:407px;display:flex;align-items:center;gap:7px}
.hours-label{font-weight:800;font-size:15px;line-height:15px;color:var(--ink)}
.hours-label span{color:var(--blue)}
.pill{width:118px;height:13px;border-radius:7px;font-weight:700;font-size:8.5px;display:flex;align-items:center;justify-content:center;margin:2px 0}
.pill.days{background:var(--yellow);color:var(--ink)}
.pill.time{background:var(--blue);color:var(--white)}
.v-rule{width:0;height:32px;border-left:1px solid #c9cfd8}
.back-rule-1{left:233px;top:411px}
.back-rule-2{left:591px;top:411px}
.back-cta{left:243px;top:409px;font-size:16px}
.back-cta small{font-size:12px}
.back-contact{left:394px;top:409px;font-size:11.5px}
.follow{left:601px;top:412px;display:flex;align-items:center;gap:6px;font-weight:800;font-size:10px;line-height:11px;color:var(--ink)}
.social-dot{width:16px;height:16px;border-radius:50%;background:var(--royal)}
</style>
</head>
<body>

<section class="card front">
  <div class="abs front-hero"></div>
  <div class="abs photo-plumber" role="img" aria-label="Photo of a plumber repairing pipes under a kitchen sink"></div>

  <p class="abs kicker">NEED RELIABLE</p>
  <h1 class="abs headline">PLUMBING<br>SOLUTION</h1>
  <p class="abs script">for your</p>
  <p class="abs audience">HOME <span class="or-dot">OR</span> BUSINESS?</p>
  <p class="abs tagline">Your Trusted Family Plumber <span>Since 2007</span></p>

  <p class="abs serving"><span>Now Serving</span>&nbsp;You From</p>
  <ul class="abs towns">
    <li><svg width="9" height="11" viewBox="0 0 9 11"><path d="M4.5 0A4 4 0 0 0 .5 4c0 3 4 7 4 7s4-4 4-7a4 4 0 0 0-4-4zm0 5.5a1.5 1.5 0 1 1 0-3 1.5 1.5 0 0 1 0 3z" fill="#f0d31a"/></svg>Santa Rosa</li>
    <li><svg width="9" height="11" viewBox="0 0 9 11"><path d="M4.5 0A4 4 0 0 0 .5 4c0 3 4 7 4 7s4-4 4-7a4 4 0 0 0-4-4zm0 5.5a1.5 1.5 0 1 1 0-3 1.5 1.5 0 0 1 0 3z" fill="#f0d31a"/></svg>Windsor</li>
    <li><svg width="9" height="11" viewBox="0 0 9 11"><path d="M4.5 0A4 4 0 0 0 .5 4c0 3 4 7 4 7s4-4 4-7a4 4 0 0 0-4-4zm0 5.5a1.5 1.5 0 1 1 0-3 1.5 1.5 0 0 1 0 3z" fill="#f0d31a"/></svg>Petaluma</li>
    <li><svg width="9" height="11" viewBox="0 0 9 11"><path d="M4.5 0A4 4 0 0 0 .5 4c0 3 4 7 4 7s4-4 4-7a4 4 0 0 0-4-4zm0 5.5a1.5 1.5 0 1 1 0-3 1.5 1.5 0 0 1 0 3z" fill="#f0d31a"/></svg>Rohnert Park</li>
    <li><svg width="9" height="11" viewBox="0 0 9 11"><path d="M4.5 0A4 4 0 0 0 .5 4c0 3 4 7 4 7s4-4 4-7a4 4 0 0 0-4-4zm0 5.5a1.5 1.5 0 1 1 0-3 1.5 1.5 0 0 1 0 3z" fill="#f0d31a"/></svg>Sonoma</li>
    <li><svg width="9" height="11" viewBox="0 0 9 11"><path d="M4.5 0A4 4 0 0 0 .5 4c0 3 4 7 4 7s4-4 4-7a4 4 0 0 0-4-4zm0 5.5a1.5 1.5 0 1 1 0-3 1.5 1.5 0 0 1 0 3z" fill="#f0d31a"/></svg>Healdsburg</li>
  </ul>

  <div class="abs perks">
    <div class="perk"><span class="perk-icon"></span>Up-front<br>pricing</div>
    <div class="perk"><span class="perk-icon"></span>Clean,<br>respectful<br>professionals</div>
    <div class="perk"><span class="perk-icon"></span>Work<br>backed by<br>warranty</div>
    <div class="perk"><span class="perk-icon"></span>Locally<br>owned &amp;<br>family<br>operated</div>
  </div>

  <div class="abs special">
    <p class="special-top">LIMITED-TIME<br>SPECIAL!</p>
    <p class="special-offer"><sup>$</sup>25 OFF</p>
    <p class="special-sub"><b>YOUR FIRST</b><br>PLUMBING<br>SERVICE</p>
    <p class="special-note">New customers only. Must mention this card.</p>
  </div>

  <p class="abs brand front-brand"><span class="brand-dot"></span>HARLOW PIPEWORKS</p>
  <p class="abs cta front-cta">SCHEDULE YOUR<small>APPOINTMENT NOW</small></p>
  <ul class="abs contact front-contact">
    <li><svg width="11" height="11" viewBox="0 0 12 12"><circle cx="6" cy="6" r="6" fill="#1646b4"/><path d="M4 3l1 1.6-.6.8c.4.8 1 1.4 1.8 1.8l.8-.6L8.6 7.6 8 9C5.6 8.8 3.2 6.4 3 4z" fill="#fff"/></svg>(707) 555-0148</li>
    <li><svg width="11" height="11" viewBox="0 0 12 12"><circle cx="6" cy="6" r="6" fill="#1646b4"/><circle cx="6" cy="6" r="3" fill="none" stroke="#fff" stroke-width="1"/><path d="M3 6h6M6 3v6" stroke="#fff" stroke-width=".8"/></svg>www.harlowpipeworks.net</li>
  </ul>
</section>

<section class="card back">
  <div class="abs back-hero"></div>
  <h2 class="abs services-tab">SERVICES OFFERED</h2>
  <p class="abs services-title">PLUMBING SERVICES WE OFFER</p>

  <div class="abs col-rule" style="left:247px;top:90px;height:110px"></div>
  <div class="abs col-rule" style="left:478px;top:90px;height:110px"></div>
  <div class="abs col-rule" style="left:247px;top:212px;height:120px"></div>
  <div class="abs col-rule" style="left:478px;top:212px;height:120px"></div>
  <div class="abs row-rule" style="left:38px;top:204px;width:635px"></div>

  <div class="abs service" style="left:38px;top:96px">
    <p class="service-head"><span class="service-icon"></span>General Plumbing</p>
    <ul>
      <li><svg class="tick" width="8" height="8" viewBox="0 0 8 8"><circle cx="4" cy="4" r="4" fill="#f0d31a"/><path d="M2 4l1.4 1.4L6 2.8" fill="none" stroke="#0b2a66" stroke-width="1"/></svg>Leak Detection &amp; Repairs</li>
      <li><svg class="tick" width="8" height="8" viewBox="0 0 8 8"><circle cx="4" cy="4" r="4" fill="#f0d31a"/><path d="M2 4l1.4 1.4L6 2.8" fill="none" stroke="#0b2a66" stroke-width="1"/></svg>Pipe Repairs &amp; Repiping</li>
      <li><svg class="tick" width="8" height="8" viewBox="0 0 8 8"><circle cx="4" cy="4" r="4" fill="#f0d31a"/><path d="M2 4l1.4 1.4L6 2.8" fill="none" stroke="#0b2a66" stroke-width="1"/></svg>Water Line Services</li>
    </ul>
  </div>
  <div class="abs service" style="left:262px;top:96px">
    <p class="service-head"><span class="service-icon"></span>Fixtures &amp; Installations</p>
    <ul>
      <li><svg class="tick" width="8" height="8" viewBox="0 0 8 8"><circle cx="4" cy="4" r="4" fill="#f0d31a"/><path d="M2 4l1.4 1.4L6 2.8" fill="none" stroke="#0b2a66" stroke-width="1"/></svg>Faucet Repairs &amp; Replacements</li>
      <li><svg class="tick" width="8" height="8" viewBox="0 0 8 8"><circle cx="4" cy="4" r="4" fill="#f0d31a"/><path d="M2 4l1.4 1.4L6 2.8" fill="none" stroke="#0b2a66" stroke-width="1"/></svg>Toilet Repairs &amp; Installations</li>
      <li><svg class="tick" width="8" height="8" viewBox="0 0 8 8"><circle cx="4" cy="4" r="4" fill="#f0d31a"/><path d="M2 4l1.4 1.4L6 2.8" fill="none" stroke="#0b2a66" stroke-width="1"/></svg>Shower &amp; Bathtub Installations</li>
    </ul>
  </div>
  <div class="abs service" style="left:494px;top:96px">
    <p class="service-head"><span class="service-icon"></span>Water Heaters</p>
    <ul>
      <li><svg class="tick" width="8" height="8" viewBox="0 0 8 8"><circle cx="4" cy="4" r="4" fill="#f0d31a"/><path d="M2 4l1.4 1.4L6 2.8" fill="none" stroke="#0b2a66" stroke-width="1"/></svg>Traditional &amp; Tankless<br>Installations</li>
      <li><svg class="tick" width="8" height="8" viewBox="0 0 8 8"><circle cx="4" cy="4" r="4" fill="#f0d31a"/><path d="M2 4l1.4 1.4L6 2.8" fill="none" stroke="#0b2a66" stroke-width="1"/></svg>Repairs &amp; Maintenance</li>
    </ul>
  </div>

  <div class="abs service" style="left:38px;top:218px">
    <p class="service-head"><span class="service-icon"></span>Water Quality &amp; Filtration</p>
    <ul>
      <li><svg class="tick" width="8" height="8" viewBox="0 0 8 8"><circle cx="4" cy="4" r="4" fill="#f0d31a"/><path d="M2 4l1.4 1.4L6 2.8" fill="none" stroke="#0b2a66" stroke-width="1"/></svg>Water Filtration System<br>Installs</li>
      <li><svg class="tick" width="8" height="8" viewBox="0 0 8 8"><circle cx="4" cy="4" r="4" fill="#f0d31a"/><path d="M2 4l1.4 1.4L6 2.8" fill="none" stroke="#0b2a66" stroke-width="1"/></svg>Pressure Regulating Valve<br>Installation</li>
    </ul>
  </div>
  <div class="abs service" style="left:262px;top:218px">
    <p class="service-head"><span class="service-icon"></span>Sewer &amp; Drain Services</p>
    <ul>
      <li><svg class="tick" width="8" height="8" viewBox="0 0 8 8"><circle cx="4" cy="4" r="4" fill="#f0d31a"/><path d="M2 4l1.4 1.4L6 2.8" fill="none" stroke="#0b2a66" stroke-width="1"/></svg>Drain Cleaning &amp; Hydro-Scrubbing</li>
      <li><svg class="tick" width="8" height="8" viewBox="0 0 8 8"><circle cx="4" cy="4" r="4" fill="#f0d31a"/><path d="M2 4l1.4 1.4L6 2.8" fill="none" stroke="#0b2a66" stroke-width="1"/></svg>Sewer Line Repairs &amp;<br>Replacements</li>
      <li><svg class="tick" width="8" height="8" viewBox="0 0 8 8"><circle cx="4" cy="4" r="4" fill="#f0d31a"/><path d="M2 4l1.4 1.4L6 2.8" fill="none" stroke="#0b2a66" stroke-width="1"/></svg>Video Camera Inspections</li>
    </ul>
  </div>
  <div class="abs service" style="left:494px;top:218px">
    <p class="service-head"><span class="service-icon"></span>Gas Lines &amp; Boilers</p>
    <ul>
      <li><svg class="tick" width="8" height="8" viewBox="0 0 8 8"><circle cx="4" cy="4" r="4" fill="#f0d31a"/><path d="M2 4l1.4 1.4L6 2.8" fill="none" stroke="#0b2a66" stroke-width="1"/></svg>Gas Line Repairs &amp;<br>Installations</li>
      <li><svg class="tick" width="8" height="8" viewBox="0 0 8 8"><circle cx="4" cy="4" r="4" fill="#f0d31a"/><path d="M2 4l1.4 1.4L6 2.8" fill="none" stroke="#0b2a66" stroke-width="1"/></svg>Hydronic Heating Systems</li>
      <li><svg class="tick" width="8" height="8" viewBox="0 0 8 8"><circle cx="4" cy="4" r="4" fill="#f0d31a"/><path d="M2 4l1.4 1.4L6 2.8" fill="none" stroke="#0b2a66" stroke-width="1"/></svg>Boiler Installations &amp;<br>Maintenance</li>
    </ul>
  </div>

  <div class="abs trust">
    <div class="trust-name">HARLOW PIPEWORKS, INC</div>
    <div><svg width="9" height="9" viewBox="0 0 8 8"><circle cx="4" cy="4" r="4" fill="#1646b4"/><path d="M2 4l1.4 1.4L6 2.8" fill="none" stroke="#fff" stroke-width="1"/></svg>LICENSED</div>
    <div><svg width="9" height="9" viewBox="0 0 8 8"><circle cx="4" cy="4" r="4" fill="#1646b4"/><path d="M2 4l1.4 1.4L6 2.8" fill="none" stroke="#fff" stroke-width="1"/></svg>INSURED</div>
    <div><svg width="9" height="9" viewBox="0 0 8 8"><circle cx="4" cy="4" r="4" fill="#1646b4"/><path d="M2 4l1.4 1.4L6 2.8" fill="none" stroke="#fff" stroke-width="1"/></svg>GUARANTEED WORK</div>
  </div>
  <div class="abs van" role="img" aria-label="Photo of the company's branded white service van"></div>

  <div class="abs hours">
    <p class="hours-label"><span>OFFICE</span><br>HOURS</p>
    <div>
      <p class="pill days">MONDAY – FRIDAY</p>
      <p class="pill time">7:30 A.M. – 4:30 P.M</p>
    </div>
  </div>
  <div class="abs v-rule back-rule-1"></div>
  <p class="abs cta back-cta">SCHEDULE YOUR<small>APPOINTMENT NOW</small></p>
  <ul class="abs contact back-contact">
    <li><svg width="11" height="11" viewBox="0 0 12 12"><circle cx="6" cy="6" r="6" fill="#1646b4"/><path d="M4 3l1 1.6-.6.8c.4.8 1 1.4 1.8 1.8l.8-.6L8.6 7.6 8 9C5.6 8.8 3.2 6.4 3 4z" fill="#fff"/></svg>(707) 555-0148</li>
    <li><svg width="11" height="11" viewBox="0 0 12 12"><circle cx="6" cy="6" r="6" fill="#1646b4"/><circle cx="6" cy="6" r="3" fill="none" stroke="#fff" stroke-width="1"/><path d="M3 6h6M6 3v6" stroke="#fff" stroke-width=".8"/></svg>www.harlowpipeworks.net</li>
  </ul>
  <div class="abs v-rule back-rule-2"></div>
  <div class="abs follow"><p>FOLLOW<br>US ON</p><span class="social-dot"></span></div>
</section>

</body>
</html>
```